****FLYER design - LAW FIRM ADVERTISEMENT****

We are a small law firm based in Los Angeles, CA. We need an flyer used for advertising that we will be passing out. We want the flyer to be about 4in x 6in.

We want the flyer to advertise the name of our firm: MARVELLO QUINTARD LLP (no period)
- We want our group photo to take up a good portion of the flyer (although it's okay if parts of the photo have wording over it.)

COLORS: Our firm colors are different shades of steal/metal grey with a bit of a bold orange accent. Any bold writing, like our slogan, names of practice areas,... should be in orange.

We envision a horizontal lay-out of the flyer, but are open to creative options laid out vertically!

Feel free to play with the fonts, the sizing, the color combinations,...

We want the flyer to advertise our two areas of practice: PERSONAL INJURY and EMPLOYMENT LAW. Please also place each photo icon of our areas of practice somewhere around the name (ambulance photo for personal injury; person behind computer desk for employment law). The icons can be relatively small.

Under Personal Injury, please write:
If you or a loved one are suffering from an injury or wrongful death caused by the careless or intentional acts of others, then you have the right to pursue compensation for your injury, out-of-pocket expenses, lost wages, emotional anguish, and more.

Under Employment Law, please write:
Our attorneys regularly represent clients in disputes involving sex, age and race discrimination, sexual harassment, retaliatory discharge, defamation, unlawful termination, breach of employment contracts, and more.

Somewhere on the flyer, please write our slogan IN ITALICS (and probably in orange):
- You Speak. We Listen. They Pay.

In somewhat bright and bold writing, please write "CONTACT US FOR A FREE CONSULTATION TODAY!" (maybe just after our slogan?)
- And under that phrase, write:
- 752 W. Folbrook Lane, Suite 400 Beverly Hills, CA 90210
phone: 310.555.8143
fax: 310.555.9261
email: info@mqmlegal.example
web: www.mqmlegal.example

If possible, and only if there's room without it looking too busy, somewhere in the upper left corner, place our "MQM" logo.
Updates

PLEASE NOTE THAT WE CHANGED OUR GROUP PHOTO TO A SLIGHTLY EDITED ONE.  PLEASE BE SURE TO USE THE NEW ONE!!!  (We deleted the old.)

Target Market(s)

employees, lower and mid-income individuals, minority communities. However, we still want the flyer to look sleek, modern, and professional.

Industry/Entity Type

Advertising

Requirements
Must have
• Firm Name,
Photo of Partners,
Names, photos, and small description of practice areas,
Firm slogan,
"Contact us for a free consultation today!",
Firm contact info.

And only if space and overall look permits, firm "MQM" logo.

We want an overall very sleek, modern feel to our flyer. While we do want to look professional, we wanted a more approachable feel than the typical, conservative law offices.
Nice to have
• Firm "MQM" logo

Horizontal lay out, though we're open to vertical options.

```html
<!DOCTYPE html>
<html lang="en">
<head>
<meta charset="utf-8">
<title>Marvello Quintard LLP – Flyer</title>
<link rel="stylesheet" href="https://fonts.googleapis.com/css2?family=Roboto+Condensed:wght@400;700&display=swap">
<style>
  :root {
    --orange: #e27c22;
    --slate: #5b6470;
    --slate-dark: #4a525c;
    --panel-light: #eeeff1;
    --panel-mid: #c9cbcf;
    --band: rgba(98, 106, 118, 0.82);
    --white: #ffffff;
    --page: #ffffff;
  }
  * { box-sizing: border-box; margin: 0; padding: 0; }
  html, body {
    width: 1200px; height: 1200px; overflow: hidden;
    background: var(--page);
    font-family: "Roboto Condensed", "Arial Narrow", sans-serif;
  }
  .flyer {
    position: absolute; left: 211px; top: 311px;
    width: 780px; height: 519px;
    background: var(--white);
    border: 1px solid #d6d6d6;
    box-shadow: 3px 5px 8px rgba(0,0,0,0.28);
  }
  .team-photo {
    position: absolute; left: 0; top: 0; width: 512px; height: 361px;
    background: linear-gradient(160deg, #7a6148 0%, #b79a72 30%, #5c5040 55%, #3b3430 75%, #d9d3cc 100%);
  }
  .firm-band {
    position: absolute; left: 0; top: 293px; width: 512px; height: 68px;
    background: var(--band);
    display: flex; align-items: center; justify-content: center;
  }
  .firm-name {
    font-weight: 700; font-size: 42px; letter-spacing: 0.5px;
    color: #f2f3f4;
  }
  .contact {
    position: absolute; left: 0; top: 361px; width: 512px; text-align: center;
  }
  .slogan {
    margin-top: 8px;
    font-weight: 700; font-style: italic; font-size: 26px; color: var(--orange);
  }
  .cta {
    margin-top: 4px;
    font-weight: 700; font-size: 22px; color: var(--slate);
  }
  .details {
    margin: 8px auto 0; width: 376px;
    font-weight: 700; font-size: 14.5px; line-height: 18px; color: var(--slate-dark);
    text-align: left;
  }
  .details .row { display: flex; justify-content: space-between; }
  .practice-panel {
    position: absolute; left: 527px; top: 0; width: 252px; height: 517px;
    background: linear-gradient(90deg, var(--panel-mid) 0%, var(--panel-light) 45%, var(--panel-mid) 100%);
  }
  .practice {
    position: absolute; left: 16px; width: 222px;
  }
  .practice--injury { top: 31px; }
  .practice--employment { top: 293px; }
  .practice-head { display: flex; align-items: flex-end; gap: 8px; }
  .practice-icon {
    width: 86px; height: 86px; background: var(--orange);
    display: flex; align-items: center; justify-content: center; flex: none;
  }
  .practice-title {
    font-weight: 700; font-size: 18px; line-height: 17px; color: var(--orange);
    margin-bottom: 0;
  }
  .practice-text {
    margin-top: 8px;
    font-size: 13px; line-height: 18px; color: var(--slate);
  }
</style>
</head>
<body>
  <article class="flyer">
    <div class="team-photo" role="img" aria-label="Group photo of the firm's three partners standing in an elegant lobby"></div>
    <div class="firm-band"><h1 class="firm-name">MARVELLO QUINTARD LLP</h1></div>

    <section class="contact">
      <p class="slogan">YOU SPEAK. WE LISTEN. THEY PAY.</p>
      <p class="cta">Contact us for a free consultation today</p>
      <div class="details">
        <p>752 W. Folbrook Lane, Suite 400 Beverly Hills, CA 90210</p>
        <p class="row"><span>phone: 310.555.8143</span><span>email: info@mqmlegal.example</span></p>
        <p class="row"><span>fax: 310.555.9261</span><span>web: www.mqmlegal.example</span></p>
      </div>
    </section>

    <aside class="practice-panel">
      <section class="practice practice--injury">
        <div class="practice-head">
          <div class="practice-icon">
            <svg width="62" height="44" viewBox="0 0 62 44" aria-hidden="true">
              <path d="M3 6 h36 v26 H3 z M39 14 h10 l9 10 v8 H39 z" fill="none" stroke="#fff" stroke-width="3" stroke-linejoin="round"/>
              <path d="M18 11 h6 v6 h6 v6 h-6 v6 h-6 v-6 h-6 v-6 h6 z" fill="#fff"/>
              <path d="M42 17 h6 l6 7 h-12 z" fill="#fff"/>
              <circle cx="14" cy="35" r="5" fill="#fff" stroke="var(--orange)" stroke-width="2"/>
              <circle cx="48" cy="35" r="5" fill="#fff" stroke="var(--orange)" stroke-width="2"/>
            </svg>
          </div>
          <h2 class="practice-title">PERSONAL<br>INJURY</h2>
        </div>
        <p class="practice-text">If you or a loved one are suffering from an injury or wrongful death caused by the careless or intentional acts of others, then you have the right to pursue compensation for your injury, out-of-pocket expenses, lost wages, emotional anguish, and more.</p>
      </section>

      <section class="practice practice--employment">
        <div class="practice-head">
          <div class="practice-icon">
            <svg width="56" height="56" viewBox="0 0 56 56" aria-hidden="true">
              <rect x="4" y="12" width="10" height="14" fill="#fff"/>
              <rect x="2" y="28" width="30" height="3" fill="#fff"/>
              <rect x="6" y="31" width="3" height="20" fill="#fff"/>
              <rect x="26" y="31" width="3" height="20" fill="#fff"/>
              <circle cx="36" cy="10" r="6" fill="#fff"/>
              <path d="M30 18 h10 l4 16 h-10 z" fill="#fff"/>
              <path d="M30 22 l-10 5 l2 2 l10 -3 z" fill="#fff"/>
              <path d="M34 34 h10 v16 h-3 v-12 h-7 z" fill="#fff"/>
              <rect x="46" y="26" width="3" height="25" fill="#fff"/>
            </svg>
          </div>
          <h2 class="practice-title">EMPLOYMENT<br>LAW</h2>
        </div>
        <p class="practice-text">Our attorneys regularly represent clients in disputes involving sex, age and race discrimination, sexual harassment, retaliatory discharge, defamation, unlawful termination, breach of employment contracts, and more.</p>
      </section>
    </aside>
  </article>
</body>
</html>
```